Tomuvin 30ml pipette jar Mental Health

Label and Box for 30ml amber jar with pipette.
Already have a sample design, that needs to be adapted and possibly improved for the new packaging.
Dark brown letters on White Label.
The jar 30ml with pipette / dropper is amber with dark cap. Please view the photo.
Please view all the files, which I am uploading.
Please provide a mock up version.
Thank you.

Target Market(s)

Upscale women 34-59

Industry/Entity Type

Nutrition, Medical

Requirements
Must have
• Conservative, Minimalistic, Luxury
Should not have
• Leaves

```html
<!DOCTYPE html>
<html lang="en">
<head>
<meta charset="utf-8">
<title>Tomuvin 10 – Box and Label</title>
<link rel="stylesheet" href="https://fonts.googleapis.com/css2?family=Barlow:wght@400;500;600;700&family=Barlow+Condensed:wght@400;500;600;700&display=swap">
<style>
  :root {
    --bg: #ecebe8;
    --paper: #ffffff;
    --brown: #3a2317;
    --gold: #b08b5e;
    --ink: #2b2b2b;
    --muted: #5a5a5a;
    --rule: #3a2317;
  }
  * { box-sizing: border-box; margin: 0; padding: 0; }
  html, body { width: 1200px; height: 900px; overflow: hidden; background: var(--bg); }
  body { position: relative; font-family: "Barlow", sans-serif; color: var(--ink); }

  .brand { display: flex; flex-direction: column; align-items: center; gap: 8px; }
  .brand-dot { width: 34px; height: 34px; border-radius: 50%; background: var(--gold); }
  .brand-name { font-family: "Barlow", sans-serif; font-weight: 500; font-size: 19px; color: var(--brown); letter-spacing: .3px; }

  /* Box dieline */
  .box { position: absolute; left: 60px; top: 90px; display: flex; box-shadow: 0 2px 10px rgba(0,0,0,.08); }
  .panel { background: var(--paper); height: 720px; position: relative; }
  .panel-front { width: 300px; border-right: 1px dashed #c9c6c0; }
  .panel-side { width: 260px; padding: 22px 20px 18px; font-family: "Barlow Condensed", sans-serif; display: flex; flex-direction: column; }

  .panel-front .brand { position: absolute; top: 40px; left: 0; right: 0; }
  .product-title {
    position: absolute; left: 22px; top: 150px; height: 430px;
    writing-mode: vertical-rl; transform: rotate(180deg);
    font-family: "Barlow", sans-serif; font-weight: 600; font-size: 104px; line-height: 1;
    color: var(--brown); letter-spacing: 2px; text-align: center;
  }
  .strength-badge {
    position: absolute; left: 165px; top: 425px; width: 120px; height: 155px;
    background: var(--brown); color: var(--gold);
    font-family: "Barlow Condensed", sans-serif; font-weight: 700; font-size: 96px;
    display: flex; align-items: center; justify-content: center;
  }
  .front-rule { position: absolute; left: 22px; right: 22px; top: 602px; border-top: 1px solid var(--brown); }
  .tagline { position: absolute; left: 22px; top: 612px; font-size: 19px; line-height: 1.25; color: var(--ink); }
  .tagline span { color: var(--muted); display: block; }
  .volume { position: absolute; left: 0; right: 0; bottom: 16px; text-align: center; font-weight: 600; font-size: 22px; color: var(--ink); }

  .facts-title { font-weight: 700; font-size: 19px; color: var(--ink); border-bottom: 4px solid var(--rule); padding-bottom: 3px; }
  .facts-row { display: flex; justify-content: space-between; font-size: 13px; line-height: 1.35; }
  .facts-row b { font-weight: 600; }
  .facts-block { border-bottom: 1.5px solid var(--rule); padding: 4px 0; font-size: 13px; line-height: 1.3; }
  .ingredients { color: var(--muted); }
  .directions { font-size: 13.5px; line-height: 1.4; color: var(--muted); margin-top: 10px; }
  .directions b { color: var(--ink); font-weight: 600; }
  .web { font-style: italic; font-weight: 600; color: var(--ink); }
  .warning { background: var(--brown); color: #fff; font-weight: 600; font-size: 13px; line-height: 1.3; padding: 6px 8px; margin-top: 12px; }
  .fda { border: 1.5px solid var(--ink); font-size: 12px; line-height: 1.3; padding: 5px 8px; margin-top: 10px; }
  .maker { font-size: 12.5px; line-height: 1.28; color: var(--muted); margin-top: 12px; }
  .maker b { color: var(--ink); font-weight: 600; }
  .expiry { font-size: 14px; font-weight: 500; margin-top: auto; text-align: center; }

  /* Bottle label */
  .label {
    position: absolute; left: 650px; top: 260px; width: 510px; height: 380px;
    background: var(--paper); display: grid; grid-template-columns: 190px 150px 170px; grid-template-rows: 380px;
    box-shadow: 0 2px 10px rgba(0,0,0,.08);
    font-family: "Barlow Condensed", sans-serif;
  }
  .label > div { min-height: 0; overflow: hidden; }
  .label-facts { padding: 14px 10px 12px 14px; display: flex; flex-direction: column; }
  .label-facts .facts-title { font-size: 14px; border-bottom-width: 3px; }
  .label-facts .facts-row, .label-facts .facts-block { font-size: 10.5px; }
  .label-facts .warning { font-size: 10.5px; margin-top: 8px; padding: 4px 6px; }
  .label-facts .fda { font-size: 9.5px; margin-top: 7px; padding: 4px 6px; }
  .label-facts .expiry { font-size: 11px; text-align: left; }
  .label-main { padding: 34px 8px 14px; position: relative; }
  .label-main .brand-dot { width: 28px; height: 28px; }
  .label-main .brand-name { font-size: 15px; }
  .label-title { font-family: "Barlow", sans-serif; font-weight: 600; font-size: 30px; color: var(--brown); text-align: center; margin-top: 26px; letter-spacing: .5px; }
  .label-dose { display: flex; align-items: flex-end; gap: 6px; margin-top: 10px; }
  .label-dose i { flex: 1; border-top: 1px solid var(--brown); margin-bottom: 4px; }
  .label-dose span { font-family: "Barlow", sans-serif; font-size: 15px; }
  .label-main .tagline { position: static; font-family: "Barlow", sans-serif; font-size: 10.5px; margin-top: 16px; }
  .label-main .volume { font-family: "Barlow", sans-serif; font-size: 15px; bottom: 18px; }
  .label-info { padding: 14px 14px 12px 8px; }
  .label-info .directions { font-size: 11px; line-height: 1.4; margin-top: 0; }
  .label-info .maker { font-size: 10.5px; margin-top: 8px; line-height: 1.3; }
</style>
</head>
<body>

<section class="box" aria-label="Carton, front and side panels">
  <div class="panel panel-front">
    <div class="brand"><span class="brand-dot"></span><span class="brand-name">Stillwell Clinics</span></div>
    <h1 class="product-title">TOMUVIN</h1>
    <div class="strength-badge">10</div>
    <div class="front-rule"></div>
    <p class="tagline">Doctor Formulated<span>Developed in Clinical Practice</span></p>
    <p class="volume">30ml</p>
  </div>

  <div class="panel panel-side">
    <h2 class="facts-title">PRODUCT FACTS</h2>
    <div class="facts-block">
      <div class="facts-row"><b>Serving Size:</b><span>1 pipette/20 drops</span></div>
      <div class="facts-row"><b>Servings per Container:</b><span>30</span></div>
    </div>
    <div class="facts-block"><b>Active Formula:</b> 280mg (% of Daily Value not Established)</div>
    <div class="facts-block ingredients">Pyridoxine, Cobalamin, Folic Acid, Cannabidiol, Aroma Lemon, Aroma Orange, Hemp oil, Lithium Orotate.</div>
    <p class="directions"><b>Directions:</b> Shake well to mix ingredients before use. Take one pipette or more after meals. Adjust daily dose to your needs. Do not exceed four pipettes per day.<br><b>EU only:</b> Apply content to clean dry skin. For external use. For best results visit<br><span class="web">www.stillwell-clinics.example</span></p>
    <p class="warning">Warning: Not to be used by children under 18 years, women who are pregnant or breastfeeding.</p>
    <p class="fda">The FDA has not evaluated these statements. This product is not intended to diagnose, treat, cure, or prevent any disease.</p>
    <p class="maker">Manufactured in the EU for<br><b>Stillwell Clinics, LLC</b><br>Boulder Ridge, Colorado, USA<br>Ph. 555-010-2233 · www.stillwell-clinics.example<br><b>EU Distribution by Verdant Lab, Eood</b><br>12 Linden St., Plovdiv, Bulgaria<br>Ph. 359-000111222</p>
    <p class="expiry">exp. 10.2025</p>
  </div>
</section>

<section class="label" aria-label="Bottle label">
  <div class="label-facts">
    <h2 class="facts-title">PRODUCT FACTS</h2>
    <div class="facts-block">
      <div class="facts-row"><b>Serving Size:</b><span>1 pipette/20 drops</span></div>
      <div class="facts-row"><b>Servings per Container:</b><span>30</span></div>
    </div>
    <div class="facts-block"><b>Active Formula:</b> 280mg (% of Daily Value not Established)</div>
    <div class="facts-block ingredients">Pyridoxine, Cobalamin, Folic Acid, Cannabidiol, Aroma Lemon, Aroma Orange, Hemp oil, Lithium Orotate.</div>
    <p class="warning">Warning: Not to be used by children under 18 years, women who are pregnant or breastfeeding.</p>
    <p class="fda">The FDA has not evaluated these statements. This product is not intended to diagnose, treat, cure, or prevent any disease.</p>
    <p class="expiry">exp. 10.2025</p>
  </div>

  <div class="label-main">
    <div class="brand"><span class="brand-dot"></span><span class="brand-name">Stillwell Clinics</span></div>
    <h1 class="label-title">TOMUVIN</h1>
    <div class="label-dose"><i></i><span>10mg</span></div>
    <p class="tagline">Doctor Formulated<span>Developed in Clinical Practice</span></p>
    <p class="volume">30ml</p>
  </div>

  <div class="label-info">
    <p class="directions"><b>Directions:</b> Shake well to mix ingredients before use. Take one pipette or more after meals. Adjust daily dose to your needs. Do not exceed four pipettes per day.<br><b>EU only:</b> Apply content to clean dry skin. For external use. For best results visit <span class="web">www.stillwell-clinics.example</span></p>
    <p class="maker">Manufactured in the EU for <b>Stillwell Clinics, LLC</b> Boulder Ridge, Colorado, USA<br>Ph. 555-010-2233<br><b>EU Distribution by Verdant Lab, Eood</b> 12 Linden St., Plovdiv, Bulgaria<br>Ph. 359-000111222</p>
  </div>
</section>

</body>
</html>
```